Letterhead for Business Law Firm

We need a letter head for our firm based on the design we have settled on and it is attached. Our clients are small and large businesses around the world, and our letterhead is used typically for formal legal purposes such as demand letters (accusing the recipient of doing bad things) or responding to demand letters. It may also be sent to regulators and other government agencies. So this needs to be tasteful, but a little edgy as well - we try to convey that we are a firm that is different - businesses and investors come to us for creative, quick advice, typically in high stress circumstances, and for our ability to work through high conflict situations, and rapid paced engagements.

Target Market(s)

Lawyers, business executives, investors, government regulators who may receive letters from this firm on behalf of its clients.

Industry/Entity Type

Business

Requirements
Must have
• The design and the firm's contact information:
• Quillfen Law Firm, P.C.
• 8716 SW 19th Ave
• Portland, OR 97058
• phone: 971 555 0143
• fax: 971 555 0178
• in what placement and how depicted (e.g. a phone icon instead of the word "phone") I leave to your creative ideas.
Nice to have
• design and information can be placed at the top, bottom and/or sides of the letter, and the design should be for a standard letter size paper - and can have a separate design for the second page.

```html
<!DOCTYPE html>
<html lang="en">
<head>
<meta charset="utf-8">
<title>Quillfen Law Firm, P.C. — Letterhead</title>
<link rel="stylesheet" href="https://fonts.googleapis.com/css2?family=Open+Sans:wght@400&display=swap">
<style>
  :root {
    --paper-top: #ffffff;
    --paper-bottom: #eeeeee;
    --ink: #3a3a3a;
    --mark-ink: #1d1a1c;
    --ghost-ink: #e4e7e8;
    --teal: #4a7a80;
    --tab-dark: #141214;
    --icon: #4f6e73;
  }
  * { margin: 0; padding: 0; box-sizing: border-box; }
  html, body { width: 933px; height: 1200px; overflow: hidden; background: #ffffff; }
  .letterhead {
    position: relative;
    width: 933px;
    height: 1200px;
    background: linear-gradient(160deg, var(--paper-top) 0%, var(--paper-top) 30%, var(--paper-bottom) 100%);
    font-family: "Open Sans", sans-serif;
    color: var(--ink);
  }
  .firm-name {
    position: absolute;
    top: 48px;
    left: 0;
    width: 100%;
    text-align: center;
    font-size: 34px;
    font-weight: 400;
    letter-spacing: 10px;
    color: var(--mark-ink);
  }
  .firm-name-ghost {
    position: absolute;
    top: 548px;
    left: 0;
    width: 100%;
    text-align: center;
    font-size: 92px;
    font-weight: 400;
    letter-spacing: 22px;
    color: var(--ghost-ink);
  }
  .tab-left {
    position: absolute;
    left: 0;
    top: 1063px;
    width: 12px;
    height: 124px;
    background: var(--teal);
    border-radius: 0 7px 7px 0;
  }
  .tab-right {
    position: absolute;
    right: 0;
    top: 1128px;
    width: 15px;
    height: 52px;
    background: var(--tab-dark);
    border-radius: 7px 0 0 7px;
  }
  .contact-list {
    position: absolute;
    left: 25px;
    top: 1080px;
    list-style: none;
    font-size: 15px;
    line-height: 22px;
  }
  .contact-list li { display: flex; align-items: center; white-space: nowrap; }
  .contact-list svg { width: 14px; height: 14px; margin-right: 6px; fill: var(--icon); flex: none; }
  .address {
    position: absolute;
    right: 30px;
    top: 1137px;
    text-align: right;
    font-size: 15px;
    line-height: 22px;
    font-style: normal;
    white-space: nowrap;
  }
</style>
</head>
<body>
<main class="letterhead">
  <div class="firm-name">QUILLFEN</div>
  <div class="firm-name-ghost" aria-hidden="true">QUILLFEN</div>

  <div class="tab-left"></div>
  <div class="tab-right"></div>

  <ul class="contact-list">
    <li>
      <svg viewBox="0 0 16 16" aria-label="Phone"><path d="M8 0a8 8 0 1 0 0 16A8 8 0 0 0 8 0zm0 1.5a6.5 6.5 0 1 1 0 13 6.5 6.5 0 0 1 0-13zM5.6 4l1.4 1.6-.7 1c.6 1.3 1.5 2.2 2.7 2.8l1-.7L11.6 10l-1 1.4C7.4 11 5 8.6 4.6 5z"/></svg>
      971 555 0143
    </li>
    <li>
      <svg viewBox="0 0 16 16" aria-label="Fax"><path d="M4 0h6l2 2v4h1.5A2.5 2.5 0 0 1 16 8.5V14H0V8.5A2.5 2.5 0 0 1 2.5 6H4zm1.5 1.5V6h5V2.6l-1.1-1.1zM2.5 7.5a1 1 0 0 0-1 1v4h13v-4a1 1 0 0 0-1-1zM3 9h4v1.5H3zm7 0h1.5v1.5H10zm2 0h1.5v1.5H12z"/></svg>
      971 555 0178
    </li>
    <li>
      <svg viewBox="0 0 16 16" aria-label="Email"><path d="M8 1 0 6v9h16V6zm0 2 5.8 3.6L8 10 2.2 6.6zM1.5 8l6.5 4 6.5-4v5.5h-13z"/></svg>
      info@quillfenlaw.com
    </li>
    <li>
      <svg viewBox="0 0 16 16" aria-label="Website"><path d="M8 0a8 8 0 1 0 0 16A8 8 0 0 0 8 0zm-.7 1.6v3.1H5.1C5.6 3 6.4 1.9 7.3 1.6zm1.4 0c.9.3 1.7 1.4 2.2 3.1H8.7zM4.6 2.2c-.3.7-.6 1.5-.8 2.5H2.4a6.5 6.5 0 0 1 2.2-2.5zm6.8 0a6.5 6.5 0 0 1 2.2 2.5h-1.4c-.2-1-.5-1.8-.8-2.5zM1.8 6.1h1.8l-.1 1.2h-1.9zm3.2 0h2.3v1.2H4.9zm3.7 0H11l.1 1.2H8.7zm3.8 0h1.8l.2 1.2h-1.9zM1.6 8.7h1.9l.1 1.2H1.8zm3.3 0h2.4v1.2H5zm3.8 0h2.4l-.1 1.2H8.7zm3.8 0h1.9l-.2 1.2h-1.8zM2.4 11.3h1.4c.2 1 .5 1.8.8 2.5a6.5 6.5 0 0 1-2.2-2.5zm2.7 0h2.2v3.1c-.9-.3-1.7-1.4-2.2-3.1zm3.6 0h2.2c-.5 1.7-1.3 2.8-2.2 3.1zm3.5 0h1.4a6.5 6.5 0 0 1-2.2 2.5c.3-.7.6-1.5.8-2.5z"/></svg>
      www.quillfenlaw.com
    </li>
  </ul>

  <address class="address">
    8716 SW 19th Ave<br>
    Portland, OR 97058
  </address>
</main>
</body>
</html>
```